Business Card Design needed for start up company Pelmora

In need of a new business card designed for a start up company based in Sydney, Pelmora is a new start up innovative Company, our mission it to make property accessible for everyday Australian and to become the leading Real Estate platform in Australia. We want it to be fresh and clean.

Industry/Entity Type

Financial

Contact Information for Business Card

Section for Name
Section for Title

PELMORA - Keys Within Reach
Mobile:
Direct:

Font styles to use
Sans Serif

Colors
33a6d7
0692cd
0255a3
ffffff

Requirements
Must have
• Logo, all business card details

```html
<!DOCTYPE html>
<html lang="en">
<head>
<meta charset="utf-8">
<title>Pelmora Business Card</title>
<link rel="stylesheet" href="https://fonts.googleapis.com/css2?family=Lato:wght@400;700&display=swap">
<style>
  :root {
    --stage: #2b2b2b;
    --sky: #33a6d7;
    --ocean: #0692cd;
    --navy: #0255a3;
    --deep: #163d73;
    --paper: #ffffff;
    --ink: #1f3354;
  }
  * { box-sizing: border-box; margin: 0; padding: 0; }
  html, body { width: 1200px; height: 873px; overflow: hidden; }
  body {
    background: var(--stage);
    font-family: "Lato", Arial, sans-serif;
    position: relative;
  }
  .card {
    position: absolute;
    width: 560px;
    height: 320px;
    border-radius: 18px;
    overflow: hidden;
    box-shadow: 0 18px 40px rgba(0,0,0,.45);
  }
  .card-front { left: 70px; top: 70px; background: var(--navy); }
  .card-back  { left: 570px; top: 483px; background: var(--paper); }

  .facet-texture {
    position: absolute; inset: 0;
    background: linear-gradient(135deg, #1a6bbf 0%, var(--navy) 45%, #0a4a8f 100%);
  }
  .brand {
    position: absolute;
    display: flex; align-items: center; gap: 12px;
  }
  .brand-dot { width: 58px; height: 58px; border-radius: 50%; background: var(--sky); flex: none; }
  .brand-name { font-weight: 700; letter-spacing: 1px; line-height: 1; }
  .card-front .brand { left: 50%; top: 50%; transform: translate(-50%, -50%); }
  .card-front .brand-name { color: var(--paper); font-size: 64px; }
  .card-back .brand { left: 40px; top: 132px; }
  .card-back .brand-dot { width: 48px; height: 48px; }
  .card-back .brand-name { color: var(--deep); font-size: 46px; }

  .details {
    position: absolute; right: 34px; top: 32px;
    text-align: right;
  }
  .person-name { color: var(--deep); font-weight: 700; font-size: 17px; }
  .person-title { color: var(--ocean); font-size: 12px; margin-top: 1px; }
  .address { color: var(--ocean); font-weight: 700; font-size: 12.5px; line-height: 1.35; margin-top: 36px; margin-right: 30px; }
  .contact-list { list-style: none; margin-top: 8px; }
  .contact-list li {
    display: flex; justify-content: flex-end; align-items: center; gap: 8px;
    color: var(--ink); font-size: 13px; height: 23px;
  }
  .icon { width: 22px; height: 22px; flex: none; }
  .email { color: var(--ink); font-size: 13px; margin-top: 10px; }
  .website { color: var(--ocean); font-weight: 700; font-size: 13px; letter-spacing: 4px; margin-top: 10px; }
</style>
</head>
<body>
  <section class="card card-front">
    <div class="facet-texture" role="img" aria-label="Faceted low-poly texture in shades of blue"></div>
    <div class="brand">
      <span class="brand-dot"></span>
      <span class="brand-name">PELMORA</span>
    </div>
  </section>

  <section class="card card-back">
    <div class="brand">
      <span class="brand-dot"></span>
      <span class="brand-name">PELMORA</span>
    </div>
    <div class="details">
      <p class="person-name">Clara Brennan</p>
      <p class="person-title">CEO &amp; Managing Director</p>
      <p class="address">Level 4, 18 Harlow Street<br>Sydney 2000 NSW</p>
      <ul class="contact-list">
        <li>02 5550 1427
          <svg class="icon" viewBox="0 0 22 22"><circle cx="11" cy="11" r="11" fill="#0255a3"/><path d="M6 9c0-2 2-3 5-3s5 1 5 3l-2 1-1-2h-4l-1 2zM7 11h8l1 5H6z" fill="#fff"/></svg>
        </li>
        <li>1300 555 218
          <svg class="icon" viewBox="0 0 22 22"><circle cx="11" cy="11" r="11" fill="#0255a3"/><rect x="7" y="5" width="8" height="4" fill="#fff"/><rect x="5" y="9" width="12" height="6" rx="1" fill="#fff"/><rect x="7" y="13" width="8" height="4" fill="#fff"/></svg>
        </li>
        <li class="email">info@pelmora.com.au
          <svg class="icon" viewBox="0 0 22 22"><circle cx="11" cy="11" r="11" fill="#0255a3"/><rect x="5" y="7" width="12" height="8" fill="#fff"/><path d="M5 7l6 5 6-5" fill="none" stroke="#0255a3" stroke-width="1.2"/></svg>
        </li>
      </ul>
      <p class="website">www.pelmora.com</p>
    </div>
  </section>
</body>
</html>
```